Long Term Insurance for Maturing Women

My business, is a Full service Life and Property Insurance Agency.. I want a reply card, Gloss, with woman showing Maturity, on a beach looking out at a Sun Set, with light Colors of Rainbow.
Thinking: If I am alone, how much income will I need to pay for a Long Term Sickness or Injury. ?
Do I have enough money set aside to cover the added expenses of a long Term Illness ?
Have I enough Life Insurance to cover final expenses, and leave my love ones free of any Debt from my Passing ?
These are real life's concerns, Please Call, let's start finding answers today !
Mark Doverby, Agent # 0718243 at (555-203-4817) - Halvert Insurance & Financial Service LLC.
Markdov@halvertins.example 4100 Birchwell Rd, Cypress Ca. 90000

Industry/Entity Type

Business

```html
<!DOCTYPE html>
<html lang="en">
<head>
<meta charset="utf-8">
<title>Reply Card – Halvert Insurance &amp; Financial Service LLC</title>
<link rel="stylesheet" href="https://fonts.googleapis.com/css2?family=Quicksand:wght@500;600;700&family=Open+Sans:wght@400;700&display=swap">
<style>
  :root {
    --paper: #ffffff;
    --mark: #111111;
    --sky-top: #1f6fb8;
    --sky-mid: #7fb2dc;
    --sky-pale: #dfe6ea;
    --glow: #f7c64a;
    --horizon: #e8742a;
    --land: #3b2520;
    --land-deep: #22150f;
    --band: rgba(190, 200, 235, 0.38);
    --frame: rgba(255, 255, 255, 0.75);
    --question: #f6dcc6;
    --call: #6b2a12;
    --contact: #ffffff;
  }
  * { margin: 0; padding: 0; box-sizing: border-box; }
  html, body { width: 1200px; height: 843px; overflow: hidden; background: var(--paper); }
  .sheet { position: relative; width: 1200px; height: 843px; }
  .crop-marks { position: absolute; inset: 0; }
  .card {
    position: absolute; left: 101px; top: 93px; width: 982px; height: 654px;
    overflow: hidden;
  }
  .sunset-photo {
    position: absolute; inset: 0;
    background:
      linear-gradient(180deg, transparent 0%, transparent 74%, rgba(59,37,32,0.85) 76%, var(--land) 84%, var(--land-deep) 100%),
      linear-gradient(180deg, var(--sky-top) 0%, var(--sky-mid) 32%, var(--sky-pale) 55%, var(--glow) 68%, var(--horizon) 75%, var(--land) 100%);
  }
  .side-band {
    position: absolute; left: 42px; top: 0; width: 230px; height: 100%;
    background: var(--band);
  }
  .connectors { position: absolute; inset: 0; }
  .questions {
    position: absolute; right: 46px; top: 54px;
    font-family: "Quicksand", sans-serif; font-weight: 700;
    font-size: 20px; line-height: 39px; letter-spacing: 0.4px;
    color: var(--question); text-align: right; white-space: nowrap;
  }
  .call-to-action {
    position: absolute; right: 53px; top: 285px;
    font-family: "Quicksand", sans-serif; font-weight: 600;
    font-size: 24px; line-height: 35px;
    color: var(--call); text-align: right; white-space: nowrap;
  }
  .contact {
    position: absolute; right: 728px; top: 0;
    font-family: "Open Sans", sans-serif; color: var(--contact);
    text-align: right; white-space: nowrap;
  }
  .contact p { position: absolute; right: 0; }
  .agent-name { top: 356px; font-size: 16px; font-weight: 700; line-height: 20px; }
  .agent-number { top: 379px; font-size: 11px; line-height: 14px; }
  .agent-phone { top: 416px; font-size: 15px; line-height: 20px; }
  .agency { top: 459px; font-size: 15px; line-height: 22px; }
  .agent-email { top: 528px; font-size: 14px; line-height: 20px; }
  .agency-address { top: 568px; font-size: 15px; line-height: 22px; }
</style>
</head>
<body>
<div class="sheet">
  <svg class="crop-marks" width="1200" height="843" viewBox="0 0 1200 843" aria-hidden="true">
    <g stroke="var(--mark)" stroke-width="2">
      <line x1="132" y1="16" x2="132" y2="76"/>
      <line x1="1079" y1="16" x2="1079" y2="76"/>
      <line x1="132" y1="764" x2="132" y2="826"/>
      <line x1="1079" y1="764" x2="1079" y2="826"/>
      <line x1="33" y1="106" x2="95" y2="106"/>
      <line x1="1105" y1="106" x2="1167" y2="106"/>
      <line x1="33" y1="733" x2="95" y2="733"/>
      <line x1="1105" y1="733" x2="1167" y2="733"/>
    </g>
  </svg>

  <section class="card">
    <div class="sunset-photo" role="img" aria-label="Photograph of a mature woman with wind-blown hair and sunglasses on a cliff, looking out over a canyon at a sunset sky"></div>
    <div class="side-band"></div>

    <svg class="connectors" width="982" height="654" viewBox="0 0 982 654" aria-hidden="true">
      <g fill="none" stroke="var(--frame)" stroke-width="2">
        <rect x="332" y="42" width="621" height="188" rx="26"/>
        <rect x="332" y="230" width="621" height="186" rx="26"/>
        <rect x="51" y="340" width="215" height="296" rx="42"/>
        <line x1="202" y1="229" x2="940" y2="229"/>
      </g>
      <g fill="#ffffff">
        <circle cx="331" cy="172" r="7"/>
        <circle cx="202" cy="229" r="7"/>
        <circle cx="331" cy="294" r="7"/>
      </g>
    </svg>

    <div class="questions">
      <p>Do I have enough savings?</p>
      <p>Do I have enough to cover any uncentities in the future?</p>
      <p>Do I have enough life insurace to cover&nbsp; all my</p>
      <p>expensives so as not to leave my love ones dept free?</p>
    </div>

    <div class="call-to-action">
      <p>These are real life's concerns,&nbsp;</p>
      <p>Please Call, let's start finding answers today</p>
    </div>

    <address class="contact" style="font-style: normal;">
      <p class="agent-name">Mark Doverby</p>
      <p class="agent-number">Agent # 0718243</p>
      <p class="agent-phone">(555)-203-4817</p>
      <p class="agency">Halvert Insurance &amp;&nbsp;<br>Financial Service LLC</p>
      <p class="agent-email">Markdov@halvertins.example</p>
      <p class="agency-address">4100 Birchwell Rd<br>Cypress Ca. 90000</p>
    </address>
  </section>
</div>
</body>
</html>
```